Label Design Refresh for existing High End Supplement line

Design a label for our high end supplement brand, packaged in a Cobal Blue bottle.... using Clear labels as the label stock media.

A clear label design will take advantage of the blue bottle and can incorporate any design element you create, metalic elements, new graphics etc.

our line spans 50 different product categories and over 400 unique SKUs, so any elements you suggest to differentiate products or categories will be appreciated.

see: www.velmorahealth.com
Updates

Need designers to meet project requirements. Full label, clear label stock design (clear background with exception for design elements and text etc.)

Target Market(s)

Men and Women 25-55 Health conscious and not price sensitive. Product is 5x higher cost than competition.

Industry/Entity Type

Sexual health for men and women. testosterone, hormone health, nootropics

Font styles to use
Sans Serif

Colors

Designer to choose colors to be used in the design.

Requirements
Must have
• Clear label design for Cobalt blue, packer style, pharma bottle. Must feature Velmora brand on front panel. Must show entire label panel design as 2.8in x 7.25in. Graphics can be full color with metalic or foil type elements.
Nice to have
• Name of products include: SHBG, Testosterone & Libido, Adrenal Support Phase 2, LH Formula, ADHD Phase1,
Should not have
• Busy designs that are stock images for supplement label layouts

```html
<!DOCTYPE html>
<html lang="en">
<head>
<meta charset="utf-8">
<title>Velmora SHBG – Label Panel</title>
<link href="https://fonts.googleapis.com/css2?family=Bebas+Neue&family=Montserrat:wght@400;500;700;800;900&family=Poppins:wght@400;500;600;700;800&display=swap" rel="stylesheet">
<style>
  :root {
    --canvas: #c9c9c9;
    --brand-blue: #1279db;
    --deep-blue: #1d5fb8;
    --ink: #1e1e1e;
    --body: #2a2a2a;
    --slate: #5c6877;
    --white: #ffffff;
    --rule: #3a3a3a;
  }
  * { margin: 0; padding: 0; box-sizing: border-box; }
  html, body { width: 1200px; height: 860px; overflow: hidden; background: var(--canvas); }
  body { position: relative; font-family: "Poppins", sans-serif; color: var(--body); }

  .label {
    position: absolute; left: 40px; top: 214px;
    width: 1120px; height: 432px;
  }
  .label__bands { position: absolute; inset: 0; width: 100%; height: 100%; }
  .abs { position: absolute; }

  /* Left panel – supplement facts */
  .facts {
    left: 51px; top: 52px; width: 262px; height: 250px;
    border: 1.5px solid var(--ink); background: var(--white);
  }
  .facts__title {
    height: 35px; background: var(--ink); color: var(--white);
    font: 700 21px/35px "Poppins", sans-serif; padding-left: 8px; letter-spacing: .2px;
    white-space: nowrap;
  }
  .facts__serving {
    margin: 8px 0 0 8px; width: 150px; padding-bottom: 5px;
    border-bottom: 1.5px solid var(--ink);
    font: 600 8.3px/10px "Poppins", sans-serif; color: var(--ink);
    white-space: nowrap;
  }
  .facts__table {
    left: 10px; top: 91px; width: 237px; height: 124px;
    border: 1.2px solid var(--ink);
  }
  .facts__table-head { height: 20px; background: var(--ink); }
  .facts__rows {
    display: grid; grid-template-columns: 135px 48px 23px 1fr;
    height: 102px; font: 400 6.6px/11.6px "Poppins", sans-serif; color: var(--ink);
  }
  .facts__col { padding-top: 6px; border-right: 1px solid var(--ink); white-space: nowrap; }
  .facts__col:last-child { border-right: 0; }
  .facts__col--name { padding-left: 6px; }
  .facts__col--amt, .facts__col--unit, .facts__col--dv { text-align: center; font-weight: 600; }
  .facts__col small { font-size: 4.8px; }
  .facts__note { left: 10px; top: 221px; font: 500 5.4px "Poppins", sans-serif; color: var(--ink); }
  .facts__other { left: 10px; top: 230px; font: 500 7.4px "Poppins", sans-serif; color: var(--ink); white-space: nowrap; }

  .left-caption {
    left: 51px; top: 323px; width: 262px;
    font: 700 8px/10.5px "Montserrat", sans-serif; color: var(--ink); text-align: justify;
  }
  .seal-notice {
    left: 51px; top: 361px; width: 262px; height: 33px;
    background: var(--brand-blue); color: var(--white);
    font: 700 9.6px/33px "Poppins", sans-serif; text-align: center; letter-spacing: -.1px;
    white-space: nowrap;
  }

  /* Front panel */
  .brand-name {
    left: 383px; top: 212px; width: 364px; height: 54px;
    transform: translate(-50%, -50%) rotate(-90deg);
    font: 700 71px/54px "Poppins", sans-serif; color: var(--slate);
    text-align: center; letter-spacing: -1px; white-space: nowrap;
  }
  .product-name {
    left: 440px; top: 48px;
    font: 400 151px/1 "Bebas Neue", sans-serif; letter-spacing: 11px;
    color: var(--deep-blue);
  }
  .product-claim {
    left: 443px; top: 178px;
    font: 700 16.8px "Poppins", sans-serif; color: var(--ink); letter-spacing: .1px;
    white-space: nowrap;
  }
  .formula-list {
    left: 444px; top: 252px; width: 186px; height: 99px;
    border-left: 1.5px solid var(--deep-blue); list-style: none;
  }
  .formula-list li {
    width: 186px;
    font: 400 14.6px "Poppins", sans-serif; color: var(--body);
    padding-left: 6px; height: 33px; line-height: 29px;
    white-space: nowrap; overflow: visible;
  }
  .formula-list li + li { border-top: 2px solid var(--brand-blue); }
  .formula-list li:first-child { height: 31px; }
  .supplement-type {
    left: 443px; top: 383px;
    font: 500 10px "Montserrat", sans-serif; letter-spacing: 2.9px; color: var(--ink);
    white-space: nowrap;
  }
  .count { left: 681px; top: 370px; font: 700 40px/1 "Poppins", sans-serif; color: var(--white); }
  .count__unit {
    left: 734px; top: 376px;
    font: 800 16.5px/16px "Poppins", sans-serif; color: var(--white);
    white-space: nowrap;
  }

  /* Right panel */
  .info { left: 824px; width: 270px; font: 400 10px/12px "Montserrat", sans-serif; color: var(--body); text-align: justify; }
  .info b { font-weight: 900; color: var(--brand-blue); font-size: 12px; letter-spacing: .2px; }
  .info--use { top: 52px; }
  .info--warn { top: 121px; }
  .info--disc { top: 222px; }
  .rule { left: 824px; width: 270px; height: 1px; background: var(--rule); }
  .batch { left: 824px; top: 318px; font: 700 8px/10px "Poppins", sans-serif; color: var(--ink); }
  .batch-box { left: 1007px; top: 304px; width: 89px; height: 31px; background: #000; }
</style>
</head>
<body>
  <main class="label">
    <svg class="label__bands" viewBox="0 0 1120 432" preserveAspectRatio="none" aria-hidden="true">
      <defs>
        <linearGradient id="silver" x1="0" y1="0" x2="1" y2="0">
          <stop offset="0" stop-color="#8d8d8d"/>
          <stop offset=".35" stop-color="#e2e2e2"/>
          <stop offset=".7" stop-color="#9c9c9c"/>
          <stop offset="1" stop-color="#707070"/>
        </linearGradient>
        <linearGradient id="front" x1="0" y1="0" x2="1" y2="1">
          <stop offset="0" stop-color="#f3f4f5"/>
          <stop offset="1" stop-color="#d5d8dd"/>
        </linearGradient>
      </defs>
      <rect x="0" y="0" width="1120" height="432" fill="#ffffff"/>
      <rect x="318" y="0" width="456" height="432" fill="url(#front)"/>
      <rect x="0" y="0" width="1120" height="10" fill="#1279db"/>
      <rect x="0" y="0" width="318" height="33" fill="#1279db"/>
      <polygon points="318,0 351,0 351,16 333,33 318,33" fill="#1279db"/>
      <rect x="351" y="10" width="769" height="6" fill="url(#silver)"/>
      <rect x="0" y="405" width="680" height="14" fill="url(#silver)"/>
      <rect x="0" y="419" width="1120" height="13" fill="#1279db"/>
      <polygon points="680,352 1120,352 1120,432 638,432" fill="#1279db"/>
    </svg>

    <!-- Left panel -->
    <section class="abs facts">
      <h2 class="facts__title">SUPPLEMENTAL FACTS</h2>
      <p class="facts__serving">Serving Size: 2 vegetable capsules<br>Servings Per Container: 30<br>Capsules: 60 capsules</p>
      <div class="abs facts__table">
        <div class="facts__table-head"></div>
        <div class="facts__rows">
          <div class="facts__col facts__col--name">Vitamin C<br>Echinacea 10:1<br>Andrographispaniculata10:1<br>Gingerextract <small>(Gingerols 10:1)</small><br>Elderberryfruitextract <small>(Sambucusnigra)</small><br>Vitamin D3<br>Zinc<br>Vitamin K2</div>
          <div class="facts__col facts__col--amt">400<br>300<br>200<br>150<br>150<br>30<br>11<br>75</div>
          <div class="facts__col facts__col--unit">mg<br>mg<br>mg<br>mg<br>mg<br>mcg<br>mg<br>mcg</div>
          <div class="facts__col facts__col--dv">500%<br>*<br>*<br>*<br>*<br>200%<br>100%<br>*</div>
        </div>
      </div>
      <p class="abs facts__note">*DailyValue not established</p>
      <p class="abs facts__other">Other ingredients: Vegetable Cellulose (Vegan capsules)</p>
    </section>
    <p class="abs left-caption">LOREM IPSUM DOLOR SIT AMET, CONSECTETUR ADIPISCING ELIT VELIT ESSE</p>
    <p class="abs seal-notice">DO NOT USE IF SAFETY SEAL IS DAMAGED OR MISSING</p>

    <!-- Front panel -->
    <p class="abs brand-name">VELMORA</p>
    <h1 class="abs product-name">SHBG</h1>
    <p class="abs product-claim">TESTOSTERONE &amp; LIBIDO</p>
    <ul class="abs formula-list">
      <li>ADRENAL SUPPORT PHASE 2</li>
      <li>LH FORMULA</li>
      <li>ADHD PHASE1</li>
    </ul>
    <p class="abs supplement-type">DIETARY SUPPLEMENT</p>
    <p class="abs count">60</p>
    <p class="abs count__unit">VEGETABLE<br>CAPSULES</p>

    <!-- Right panel -->
    <p class="abs info info--use"><b>SUGGESTED USE:</b> Lorem ipsum dolor sit amet, consectetur adipiscing elit, sed do eiusmod tempor incididunt ut labore et dolore magna aliqua. Ut enim</p>
    <div class="abs rule" style="top:106px"></div>
    <p class="abs info info--warn"><b>WARNINGS:</b> Lorem ipsum dolor sit amet, consectetur adipiscing elit, sed do eiusmod tempor incididunt ut labore et dolore magna aliqua. Ut enim ad minim veniam, quis nostrud exercitation ullamco laboris nisi ut aliquip ex ea commodo consequat. Duis aute irure dolor in reprehenderit</p>
    <div class="abs rule" style="top:207px"></div>
    <p class="abs info info--disc"><b>DISCLAIMER:</b> Lorem ipsum dolor sit amet, consectetur adipiscing elit, sed do eiusmod tempor incididunt ut labore et dolore magna aliqua. Ut enim ad minim veniam, quis nostrud</p>
    <div class="abs rule" style="top:281px"></div>
    <p class="abs batch">Expiration date:<br>Lot Number:</p>
    <div class="abs batch-box"></div>
  </main>
</body>
</html>
```